Mortgage Broking boutique Business

I’m wanting a revamped look to my existing business card design. I do like the black and silver but happy to have other colours introduced based on your creation. I’ve attached a copy of my current card so you can have a starting point updated details noted brloe. I deal with high net worth individuals so need my card to be sophisticated, classy that gives off a classy vibe

Target Market(s)

High net worth, wealthy

Industry/Entity Type

Mortgage Brokerage

Contact Information for Business Card

Job title: Finance Executive
Phone: +61 7 3287 4419
Mobile: 0471 352 608
Email: marcus@quillbrookcapital.com.au
Web: www.quillbrookcapital.com.au
Address: level 36 Tindale Court, 58 Harwick St Brisbane QLD 4000

Font styles to use
Other font styles liked:
• Helvetica

Colors

Designer to choose colors to be used in the design.

Requirements
Must have
• Use my existing card design as a starting point

```html
<!DOCTYPE html>
<html lang="en">
<head>
<meta charset="utf-8">
<title>Quillbrook Capital – Business Card</title>
<link href="https://fonts.googleapis.com/css2?family=Arimo:wght@400;700&display=swap" rel="stylesheet">
<style>
  :root {
    --backdrop: #4a4a4a;
    --card-top: #1d1d1d;
    --card-bottom: #0e0e0e;
    --silver: #a9a9a9;
    --silver-light: #d6d6d6;
    --ink: #f2f2f2;
    --ink-soft: #d9d9d9;
  }
  * { margin: 0; padding: 0; box-sizing: border-box; }
  html, body { width: 1200px; height: 801px; overflow: hidden; }
  body {
    background: var(--backdrop);
    font-family: "Arimo", Helvetica, Arial, sans-serif;
    position: relative;
  }
  .card {
    position: absolute;
    top: 282px;
    width: 416px;
    height: 238px;
    border-radius: 12px;
    background: linear-gradient(160deg, var(--card-top), var(--card-bottom));
  }
  .card--front { left: 150px; }
  .card--back { left: 634px; }
  .card__frame {
    position: absolute;
    inset: 22px;
    border: 1.5px solid var(--silver);
    border-radius: 8px;
  }
  .wordmark {
    position: absolute;
    color: var(--ink);
    font-weight: 400;
    text-align: center;
    text-transform: uppercase;
    line-height: 1;
  }
  .wordmark__main { display: block; letter-spacing: 0.22em; }
  .wordmark__sub { display: block; letter-spacing: 0.3em; margin-top: 6px; }
  .card--front .wordmark { left: 0; right: 0; top: 100px; }
  .card--front .wordmark__main { font-size: 20px; }
  .card--front .wordmark__sub { font-size: 11px; }
  .card--back .wordmark { left: 40px; top: 48px; }
  .card--back .wordmark__main { font-size: 16px; }
  .card--back .wordmark__sub { font-size: 10px; }
  .holder {
    position: absolute;
    right: 46px;
    top: 46px;
    text-align: right;
    color: var(--ink);
  }
  .holder__name { font-weight: 700; font-size: 16px; letter-spacing: 0.02em; }
  .holder__title { font-size: 12.5px; margin-top: 3px; color: var(--ink-soft); }
  .contacts {
    position: absolute;
    left: 207px;
    top: 116px;
    list-style: none;
  }
  .contacts li, .address {
    display: flex;
    align-items: center;
    gap: 6px;
    font-size: 10.5px;
    color: var(--ink-soft);
    height: 17px;
  }
  .contacts svg, .address svg { width: 9px; height: 9px; fill: var(--silver-light); flex: none; }
  .address { position: absolute; left: 56px; top: 196px; }
  .address svg { width: 10px; height: 12px; }
</style>
</head>
<body>
  <section class="card card--front" aria-label="Card front">
    <div class="card__frame"></div>
    <div class="wordmark">
      <span class="wordmark__main">Quillbrook</span>
      <span class="wordmark__sub">Capital</span>
    </div>
  </section>

  <section class="card card--back" aria-label="Card back">
    <div class="card__frame"></div>
    <div class="wordmark">
      <span class="wordmark__main">Quillbrook</span>
      <span class="wordmark__sub">Capital</span>
    </div>
    <div class="holder">
      <p class="holder__name">MARCUS AVERY</p>
      <p class="holder__title">Finance Executive</p>
    </div>
    <ul class="contacts">
      <li><svg viewBox="0 0 10 10"><path d="M1 3.5C1 2 2.5 1 5 1s4 1 4 2.5L7.5 4.3 6.5 3H3.5L2.5 4.3zM2 5h6l1 4H1z"/></svg>+61 7 3287 4419</li>
      <li><svg viewBox="0 0 10 10"><path d="M3 0h4a1 1 0 0 1 1 1v8a1 1 0 0 1-1 1H3a1 1 0 0 1-1-1V1a1 1 0 0 1 1-1zm0 1.5v6h4v-6zM5 8.2a.5.5 0 1 0 0 1 .5.5 0 0 0 0-1z"/></svg>0471 352 608</li>
      <li><svg viewBox="0 0 10 10"><path d="M0 2h10v.8L5 5.8 0 2.8zm0 1.9 5 3 5-3V8H0z"/></svg>marcus@quillbrookcapital.com.au</li>
      <li><svg viewBox="0 0 10 10"><path d="M5 0a5 5 0 1 0 0 10A5 5 0 0 0 5 0zm0 1c.7.6 1.2 1.8 1.3 3.5H3.7C3.8 2.8 4.3 1.6 5 1zM1 5.5h1.9c.1 1.3.4 2.4.9 3.2A4 4 0 0 1 1 5.5zm0-1a4 4 0 0 1 2.8-3.2c-.5.8-.8 1.9-.9 3.2zm2.7 1h2.6C6.2 7.2 5.7 8.4 5 9c-.7-.6-1.2-1.8-1.3-3.5zm3.4 0H9a4 4 0 0 1-2.8 3.2c.5-.8.8-1.9.9-3.2zm0-1c-.1-1.3-.4-2.4-.9-3.2A4 4 0 0 1 9 4.5z"/></svg>www.quillbrookcapital.com.au</li>
    </ul>
    <p class="address"><svg viewBox="0 0 10 12"><path d="M5 0a4 4 0 0 0-4 4c0 3 4 6.5 4 6.5S9 7 9 4a4 4 0 0 0-4-4zm0 2.3a1.7 1.7 0 1 1 0 3.4 1.7 1.7 0 0 1 0-3.4zM2 11h6v1H2z"/></svg>level 36 Tindale Court, 58 Harwick St Brisbane QLD 4000</p>
  </section>
</body>
</html>
```